Working Capital graphics

Our business advisory firm requires 9 images to be re-created and improved in the branding of our business.

The 9 images have been uploaded below and the colours and branding of the business can be found at the website www.thornwickadvisory.com.au

```html
<!DOCTYPE html>
<html lang="en">
<head>
<meta charset="utf-8">
<title>Working Capital graphics – Thornwick Advisory</title>
<link href="https://fonts.googleapis.com/css2?family=Catamaran:wght@300;400;600;700&display=swap" rel="stylesheet">
<style>
  :root {
    --blue: #00aeef;
    --blue-soft: #85d8f5;
    --orange: #f6901e;
    --orange-soft: #fac690;
    --pink: #ee1f6a;
    --ink: #2b2b2b;
    --rule: #8a8a8a;
    --white: #ffffff;
  }
  html, body { margin: 0; padding: 0; overflow: hidden; background: var(--white); }
  .canvas { width: 1200px; height: 1200px; display: block; font-family: "Catamaran", sans-serif; }
  .frame { fill: var(--white); stroke: var(--blue); stroke-width: 18; }
  .divider { stroke: var(--rule); stroke-width: 2; }
  .brand-dot { fill: var(--orange); }
  .brand-name { fill: var(--orange); font-weight: 700; font-size: 20px; }
  .spoke { stroke: var(--orange-soft); stroke-width: 58; }
  .topic { fill: var(--orange); }
  .topic-text { fill: var(--white); font-size: 21px; text-anchor: middle; }
  .strong { font-weight: 600; }
  .light { font-weight: 300; }
  .hub { fill: var(--white); stroke: var(--blue); stroke-width: 8; }
  .hub-text { fill: var(--blue); font-weight: 700; font-size: 44px; text-anchor: middle; }
  .cycle-art { fill: url(#cycleTone); }
  .chart-title { fill: var(--orange); font-weight: 700; font-size: 42px; text-anchor: middle; }
  .axis { stroke: var(--ink); stroke-width: 1.5; fill: none; }
  .tick-label { fill: var(--ink); font-size: 21px; }
  .axis-title { fill: var(--orange); font-weight: 600; font-size: 26px; text-anchor: middle; }
  .zone { fill: var(--orange); }
  .guide { stroke: var(--blue); stroke-width: 2.5; stroke-dasharray: 9 7; }
  .vector { stroke: var(--blue); stroke-width: 3; }
  .arrowhead { fill: var(--blue); }
  .origin { fill: var(--white); stroke: var(--blue); stroke-width: 7; }
  .letter { fill: var(--orange); font-weight: 600; font-size: 24px; text-anchor: middle; }
  .scenario { fill: var(--ink); font-size: 22px; }
  .step { fill: var(--orange); }
  .step-text { fill: var(--white); font-weight: 600; font-size: 16px; text-anchor: middle; }
  .lever-blue { fill: var(--blue); }
  .lever-pink { fill: var(--pink); }
  .lever-text { fill: var(--white); font-size: 16px; text-anchor: middle; }
  .link { stroke: var(--rule); stroke-width: 1.5; fill: none; }
  .node { fill: var(--ink); }
  .legend-text { fill: var(--ink); font-size: 17px; }
</style>
</head>
<body>
<svg class="canvas" viewBox="0 0 1930 1930" xmlns="http://www.w3.org/2000/svg">
  <defs>
    <marker id="tip" viewBox="0 0 10 10" refX="8" refY="5" markerWidth="5" markerHeight="5" orient="auto-start-reverse">
      <path class="arrowhead" d="M0,0 L10,5 L0,10 Z"/>
    </marker>
    <linearGradient id="cycleTone" x1="0" y1="1" x2="0" y2="0">
      <stop offset="0" stop-color="#f6901e"/>
      <stop offset="0.55" stop-color="#f8a85a"/>
      <stop offset="1" stop-color="#00aeef"/>
    </linearGradient>
  </defs>

  <rect class="frame" x="37" y="37" width="1856" height="1856" rx="80"/>
  <line class="divider" x1="966" y1="88" x2="966" y2="1843"/>
  <line class="divider" x1="88" y1="966" x2="1843" y2="966"/>

  <!-- Drivers of working capital -->
  <g class="drivers">
    <g class="brand">
      <circle class="brand-dot" cx="142" cy="168" r="18"/>
      <text class="brand-name" x="168" y="163">Thornwick</text>
      <text class="brand-name" x="168" y="184">Advisory</text>
    </g>
    <g>
      <line class="spoke" x1="527" y1="535" x2="527" y2="272"/>
      <line class="spoke" x1="527" y1="535" x2="695" y2="333"/>
      <line class="spoke" x1="527" y1="535" x2="358" y2="333"/>
      <line class="spoke" x1="527" y1="535" x2="268" y2="488"/>
      <line class="spoke" x1="527" y1="535" x2="785" y2="488"/>
      <line class="spoke" x1="527" y1="535" x2="299" y2="665"/>
      <line class="spoke" x1="527" y1="535" x2="754" y2="665"/>
      <line class="spoke" x1="527" y1="535" x2="437" y2="780"/>
      <line class="spoke" x1="527" y1="535" x2="616" y2="780"/>
    </g>
    <g>
      <circle class="topic" cx="527" cy="272" r="71"/>
      <text class="topic-text" x="525" y="252"><tspan class="strong">Supply</tspan><tspan class="strong" x="525" dy="25">Chain</tspan><tspan class="light" x="527" dy="25">Issues</tspan></text>
      <circle class="topic" cx="695" cy="333" r="71"/>
      <text class="topic-text" x="695" y="326"><tspan class="strong">Process</tspan><tspan class="light" x="695" dy="26">Issues</tspan></text>
      <circle class="topic" cx="358" cy="333" r="71"/>
      <text class="topic-text" x="353" y="328"><tspan class="strong">Terms </tspan><tspan class="light">&amp;</tspan><tspan class="strong" x="353" dy="26">Conditions</tspan></text>
      <circle class="topic" cx="268" cy="488" r="71"/>
      <text class="topic-text" x="268" y="482"><tspan class="strong">IT Systems </tspan><tspan class="light">&amp;</tspan><tspan class="strong" x="268" dy="26">Information</tspan></text>
      <circle class="topic" cx="785" cy="488" r="71"/>
      <text class="topic-text" x="785" y="482"><tspan class="strong">Forecasting</tspan><tspan class="light" x="785" dy="26">&amp; </tspan><tspan class="strong">Planning</tspan></text>
      <circle class="topic" cx="299" cy="665" r="71"/>
      <text class="topic-text" x="299" y="658"><tspan class="strong">KPIs </tspan><tspan class="light">&amp;</tspan><tspan class="light" x="299" dy="26">Measures</tspan></text>
      <circle class="topic" cx="754" cy="665" r="71"/>
      <text class="topic-text" x="754" y="658"><tspan class="strong">Customer</tspan><tspan class="light" x="754" dy="26">Management</tspan></text>
      <circle class="topic" cx="437" cy="780" r="71"/>
      <text class="topic-text" x="437" y="774"><tspan class="strong">Supplier</tspan><tspan class="light" x="437" dy="26">Management</tspan></text>
      <circle class="topic" cx="616" cy="780" r="71"/>
      <text class="topic-text" x="616" y="774"><tspan class="strong">SKU</tspan><tspan class="light" x="616" dy="26">Complexity</tspan></text>
    </g>
    <circle class="hub" cx="527" cy="535" r="124"/>
    <text class="hub-text" x="527" y="520">Working</text>
    <text class="hub-text" x="527" y="572">Capital</text>
  </g>

  <!-- Working capital cycle -->
  <g class="cycle">
    <rect class="cycle-art" x="1080" y="245" width="655" height="565" rx="40" role="img"
          aria-label="Illustration: three interlocking gears labelled Accounts Receivable, Inventory and Accounts Payable, circled by arrows showing the working capital cycle"/>
    <g class="brand">
      <circle class="brand-dot" cx="1350" cy="888" r="18"/>
      <text class="brand-name" x="1376" y="883">Thornwick</text>
      <text class="brand-name" x="1376" y="904">Advisory</text>
    </g>
  </g>

  <!-- Net working capital absorption chart -->
  <g class="absorption">
    <g class="brand">
      <circle class="brand-dot" cx="472" cy="1046" r="18"/>
      <text class="brand-name" x="498" y="1041">Thornwick</text>
      <text class="brand-name" x="498" y="1062">Advisory</text>
    </g>
    <text class="chart-title" x="527" y="1160">Net Working Capital Absorbtion</text>

    <path class="zone" d="M535,1446 L535,1294 A152,152 0 1 0 687,1446 Z"/>
    <line class="guide" x1="312" y1="1446" x2="510" y2="1446"/>
    <line class="guide" x1="535" y1="1472" x2="535" y2="1668"/>

    <path class="axis" d="M302,1232 V1668 H738"/>
    <g class="axis">
      <line x1="290" y1="1264" x2="302" y2="1264"/><line x1="290" y1="1316" x2="302" y2="1316"/>
      <line x1="290" y1="1368" x2="302" y2="1368"/><line x1="290" y1="1420" x2="302" y2="1420"/>
      <line x1="290" y1="1471" x2="302" y2="1471"/><line x1="290" y1="1523" x2="302" y2="1523"/>
      <line x1="290" y1="1575" x2="302" y2="1575"/><line x1="290" y1="1627" x2="302" y2="1627"/>
      <line x1="353" y1="1668" x2="353" y2="1680"/><line x1="426" y1="1668" x2="426" y2="1680"/>
      <line x1="499" y1="1668" x2="499" y2="1680"/><line x1="572" y1="1668" x2="572" y2="1680"/>
      <line x1="645" y1="1668" x2="645" y2="1680"/><line x1="718" y1="1668" x2="718" y2="1680"/>
    </g>
    <g class="tick-label">
      <text x="220" y="1271">450m</text><text x="220" y="1323">400m</text>
      <text x="220" y="1375">350m</text><text x="220" y="1427">300m</text>
      <text x="220" y="1478">250m</text><text x="220" y="1530">200m</text>
      <text x="220" y="1582">150m</text><text x="220" y="1634">100m</text>
    </g>
    <g class="tick-label" text-anchor="middle">
      <text x="353" y="1710">20m</text><text x="426" y="1710">25m</text>
      <text x="499" y="1708">30m</text><text x="572" y="1710">35m</text>
      <text x="645" y="1710">40m</text><text x="718" y="1710">45m</text>
    </g>
    <text class="axis-title" transform="translate(185,1420) rotate(-90)">Sales</text>
    <text class="axis-title" x="520" y="1766">Net Working Capital (NWC)</text>

    <g marker-end="url(#tip)">
      <line class="vector" x1="535" y1="1446" x2="535" y2="1252"/>
      <line class="vector" x1="535" y1="1446" x2="672" y2="1310"/>
      <line class="vector" x1="535" y1="1446" x2="730" y2="1446"/>
      <line class="vector" x1="535" y1="1446" x2="672" y2="1583"/>
      <line class="vector" x1="535" y1="1446" x2="398" y2="1583"/>
      <line class="vector" x1="535" y1="1446" x2="398" y2="1310"/>
    </g>
    <circle class="origin" cx="535" cy="1446" r="25"/>

    <text class="letter" x="535" y="1219">B</text>
    <text class="letter" x="369" y="1288">A</text>
    <text class="letter" x="699" y="1288">c</text>
    <text class="letter" x="768" y="1452">D</text>
    <text class="letter" x="699" y="1617">E</text>
    <text class="letter" x="369" y="1617">F</text>
    <text class="scenario" x="368" y="1232" text-anchor="middle">Optimal<tspan x="368" dy="26">Growth</tspan></text>
    <text class="scenario" x="768" y="1232" text-anchor="middle">Fast<tspan x="768" dy="26">Growth</tspan></text>
    <text class="scenario" x="803" y="1438">Declining<tspan x="803" dy="26">Growth</tspan></text>
    <text class="scenario" x="733" y="1607">Corporate<tspan x="733" dy="26">Stress</tspan></text>
    <text class="scenario" x="316" y="1641">Downsizing</text>
  </g>

  <!-- Value chain levers -->
  <g class="value-chain">
    <g class="brand">
      <circle class="brand-dot" cx="1350" cy="1046" r="18"/>
      <text class="brand-name" x="1376" y="1041">Thornwick</text>
      <text class="brand-name" x="1376" y="1062">Advisory</text>
    </g>

    <g>
      <path class="link" d="M1038,1324 V1363"/>
      <path class="link" d="M1210,1283 V1363 M1118,1363 V1316 H1354 V1283 M1313,1316 V1363"/>
      <path class="link" d="M1497,1283 V1363"/>
      <path class="link" d="M1666,1167 V1195 M1666,1283 V1363"/>
      <path class="link" d="M1210,1460 V1542"/>
      <path class="link" d="M1666,1460 V1542"/>
      <path class="link" d="M1765,1460 V1542"/>
      <circle class="node" cx="1118" cy="1362" r="2.5"/><circle class="node" cx="1210" cy="1362" r="2.5"/>
      <circle class="node" cx="1313" cy="1362" r="2.5"/><circle class="node" cx="1497" cy="1362" r="2.5"/>
      <circle class="node" cx="1666" cy="1362" r="2.5"/><circle class="node" cx="1210" cy="1463" r="2.5"/>
      <circle class="node" cx="1666" cy="1463" r="2.5"/><circle class="node" cx="1765" cy="1463" r="2.5"/>
    </g>

    <g>
      <polygon class="step" points="987,1363 1070,1363 1087,1411 1070,1460 987,1460 1004,1411"/>
      <polygon class="step" points="1079,1363 1162,1363 1179,1411 1162,1460 1079,1460 1096,1411"/>
      <polygon class="step" points="1171,1363 1254,1363 1271,1411 1254,1460 1171,1460 1188,1411"/>
      <polygon class="step" points="1263,1363 1346,1363 1363,1411 1346,1460 1263,1460 1280,1411"/>
      <polygon class="step" points="1355,1363 1438,1363 1455,1411 1438,1460 1355,1460 1372,1411"/>
      <polygon class="step" points="1447,1363 1530,1363 1547,1411 1530,1460 1447,1460 1464,1411"/>
      <polygon class="step" points="1539,1363 1622,1363 1639,1411 1622,1460 1539,1460 1556,1411"/>
      <polygon class="step" points="1631,1363 1714,1363 1731,1411 1714,1460 1631,1460 1648,1411"/>
      <polygon class="step" points="1723,1363 1806,1363 1823,1411 1806,1460 1723,1460 1740,1411"/>
      <text class="step-text" x="1037" y="1417">Design</text>
      <text class="step-text" x="1129" y="1397">Order /<tspan x="1129" dy="18">Material</tspan><tspan x="1129" dy="18">Planing</tspan></text>
      <text class="step-text" x="1229" y="1417">Purchasing</text>
      <text class="step-text" x="1318" y="1417">Manufact.</text>
      <text class="step-text" x="1405" y="1407">Pre-<tspan x="1405" dy="19">Assembly</tspan></text>
      <text class="step-text" x="1497" y="1417">Assembly</text>
      <text class="step-text" x="1589" y="1407">Packing /<tspan x="1589" dy="19">Shipping</tspan></text>
      <text class="step-text" x="1681" y="1417">Sales</text>
      <text class="step-text" x="1773" y="1407">After Sales<tspan x="1773" dy="19">/ Service</tspan></text>
    </g>

    <g>
      <rect class="lever-blue" x="987" y="1195" width="103" height="88" rx="5"/>
      <text class="lever-text" x="1038" y="1224"><tspan class="strong">Reduce</tspan><tspan class="light" x="1038" dy="19">Part Variants</tspan><tspan class="light" x="1038" dy="19">/ Releases</tspan></text>
      <rect class="lever-pink" x="1159" y="1087" width="103" height="88" rx="5"/>
      <text class="lever-text" x="1210" y="1116"><tspan class="strong">Modify</tspan><tspan class="light" x="1210" dy="19">Payment</tspan><tspan class="light" x="1210" dy="19">Conditions</tspan></text>
      <rect class="lever-pink" x="1159" y="1195" width="103" height="88" rx="5"/>
      <text class="lever-text" x="1210" y="1224"><tspan class="strong">Optimize</tspan><tspan class="light" x="1210" dy="19">Payment</tspan><tspan class="light" x="1210" dy="19">Processes</tspan></text>
      <rect class="lever-blue" x="1275" y="1195" width="157" height="88" rx="5"/>
      <text class="lever-text" x="1354" y="1224"><tspan class="strong">Rethink</tspan><tspan class="light" x="1354" dy="19">Delivery Schedules</tspan><tspan class="light" x="1354" dy="19">&amp; Warehousing</tspan></text>
      <rect class="lever-blue" x="1446" y="1195" width="103" height="88" rx="5"/>
      <text class="lever-text" x="1497" y="1224"><tspan class="strong">Optimize</tspan><tspan class="light" x="1497" dy="19">Product</tspan><tspan class="light" x="1497" dy="19">Testing</tspan></text>
      <rect class="lever-pink" x="1615" y="1080" width="103" height="88" rx="5"/>
      <text class="lever-text" x="1666" y="1109"><tspan class="strong">Improve</tspan><tspan class="light" x="1666" dy="19">Payment</tspan><tspan class="light" x="1666" dy="19">Themes</tspan></text>
      <rect class="lever-pink" x="1615" y="1195" width="103" height="88" rx="5"/>
      <text class="lever-text" x="1666" y="1224"><tspan class="strong">Reduce</tspan><tspan class="light" x="1666" dy="19">Due / Overdue</tspan><tspan class="light" x="1666" dy="19">Receivables</tspan></text>
      <rect class="lever-pink" x="1721" y="1195" width="103" height="88" rx="5"/>
      <text class="lever-text" x="1772" y="1224"><tspan class="strong">Establish</tspan><tspan class="light" x="1772" dy="19">New Payment</tspan><tspan class="light" x="1772" dy="19">Conditions</tspan></text>
      <rect class="lever-blue" x="1159" y="1542" width="103" height="88" rx="5"/>
      <text class="lever-text" x="1210" y="1571"><tspan class="strong">Optimize</tspan><tspan class="light" x="1210" dy="19">External</tspan><tspan class="light" x="1210" dy="19">Purchasing</tspan></text>
      <rect class="lever-blue" x="1615" y="1542" width="103" height="88" rx="5"/>
      <text class="lever-text" x="1666" y="1571"><tspan class="strong">Reduce</tspan><tspan class="light" x="1666" dy="19">Finished</tspan><tspan class="light" x="1666" dy="19">Good Stocks</tspan></text>
      <rect class="lever-blue" x="1721" y="1542" width="103" height="88" rx="5"/>
      <text class="lever-text" x="1772" y="1581"><tspan class="strong">Reduce</tspan><tspan class="strong" x="1772" dy="19">Intentory</tspan></text>
    </g>

    <g class="legend">
      <rect class="step" x="1096" y="1710" width="19" height="19" rx="2"/>
      <text class="legend-text" x="1124" y="1726">Intentory</text>
      <rect class="lever-blue" x="1207" y="1710" width="19" height="19" rx="2"/>
      <text class="legend-text" x="1235" y="1726">Payables &amp; Prepayments Made</text>
      <rect class="lever-pink" x="1454" y="1710" width="19" height="19" rx="2"/>
      <text class="legend-text" x="1482" y="1726">Receivables &amp; Prepayments Received</text>
    </g>
  </g>
</svg>
</body>
</html>
```